We need a user guide (1 pager) for end users using our metering technology (electricity & Water). The users make use of cellphones / internet or bank transfers to TOP UP their accounts. (Almost like pay as you go cellphone accounts but for electricity consumption)

Their accounts are viewable on smart devices etc....
The user guide... needs to guide them through the process on 1 HOW to register
2 How to TOP UP 3 a Brief description on how the technology works
4 Problem solving..

We need a visual application for people in the residential market. (not corporate)
I like the more informal approach ... with animated graphics.(A character)

I have attached two files . One a drawing of the concept ,the other an inclusion of the wording.

The back of the pamphlet/ guide will include standard term etc.

IMPORTANT: It is the type of document that one would put on your fridge as an easy guide to refer to.

I suggest we build a character (man/ women)

This needs to be simple, funny , informal (but not stupid)

The colour scheme can be found on our website www.farvolt.net

We need someone with pencil illustration skills
Updates

Hi Look at the new uploads...

We need a pencil illustrator that can crate a character to tell our story on our pamphlet in four easy steps..

I like the sort of character in the blue pencil on paper...   Refer back to my drawing I had posted initially

Target Market(s)

End users of a system

People living in houses that need to pay their electricity bill by making use of smart technology.

This can be old aged people up to highly skilled people...

Industry/Entity Type

Residential

Requirements
Must have
• 1 pager
back to be used to print terms and definitions etc.

Company colours www.farvolt.net with qelvo

A4 size

Visuals - animated character explaining the concepts. Think of someone trying out new technology and want to access a quick user guide !!!

Nice to have
• Design arount a character.

Maybe an animated figure explaining what we want to say
Should not have
• We dont want lengthy wording and a piece of paper peaple wont read!

```html
<!DOCTYPE html>
<html lang="en">
<head>
<meta charset="utf-8">
<title>qelvo – user guide</title>
<link rel="stylesheet" href="https://fonts.googleapis.com/css2?family=Architects+Daughter&display=swap">
<style>
  :root{
    --paper:#ffffff;
    --ink:#2b2b33;
    --navy:#1c2370;
    --lime:#9dcb2b;
    --box-blue:#3b6fd0;
    --sketch-grey:#e4e5ea;
    --sketch-grey-dark:#cfd1d8;
  }
  *{box-sizing:border-box;margin:0;padding:0}
  html,body{width:927px;height:1200px;overflow:hidden;background:var(--paper)}
  body{position:relative;font-family:"Architects Daughter",cursive;color:var(--ink)}
  .brand{position:absolute;left:0;width:927px;top:2px;text-align:center;font-size:108px;line-height:118px;color:var(--navy);letter-spacing:2px}
  .grid-line{position:absolute;background:var(--lime)}
  .grid-line.top{left:0;top:126px;width:927px;height:4px}
  .grid-line.mid{left:0;top:648px;width:927px;height:4px}
  .grid-line.vert{left:474px;top:126px;width:4px;height:1074px}
  .step-no{position:absolute;width:58px;height:58px;border:3px solid var(--lime);border-radius:50%;font-size:32px;line-height:52px;text-align:center;color:var(--navy)}
  .step-title{position:absolute;height:78px;border:3px solid var(--box-blue);color:var(--navy);line-height:72px;text-align:center;text-transform:uppercase;white-space:nowrap;overflow:hidden}
  .step-title.register{font-size:32px}
  .step-title.works{font-size:29px}
  .step-title.off{font-size:20px}
  .step-title .big{font-size:46px}
  .step-title .small{font-size:24px}
  .art{position:absolute;border-radius:10px;background:linear-gradient(180deg,var(--sketch-grey),var(--sketch-grey-dark))}
  .copy{position:absolute;font-size:13px;line-height:16.5px}
  .copy.center{text-align:center}
  .device{position:absolute;border:3px solid var(--ink);background:var(--paper);font-weight:700;white-space:nowrap}
  .phone-frame{left:508px;top:318px;width:128px;height:208px;border-radius:14px;padding:12px 8px;font-size:14px;line-height:22px}
  .monitor-frame{left:676px;top:296px;width:234px;height:170px;border-radius:8px;padding:12px 14px;font-size:15px;line-height:20px}
  .device-label{position:absolute;font-size:13px;font-weight:700;text-transform:uppercase}
  .checklist{position:absolute;left:490px;top:1028px;width:430px;font-size:13px}
  .checklist h3{font-weight:400;font-size:14px;margin-bottom:6px}
  .check{display:flex;align-items:center;gap:10px;margin:6px 0 8px 4px}
  .check svg{flex:none}
  .call{text-align:center;line-height:16px;font-size:12.5px;white-space:nowrap}
</style>
</head>
<body>
  <div class="brand">qelvo</div>

  <div class="grid-line top"></div>
  <div class="grid-line mid"></div>
  <div class="grid-line vert"></div>

  <div class="step-no" style="left:24px;top:190px">1</div>
  <div class="step-title register" style="left:104px;top:189px;width:350px">How to register</div>
  <div class="art" style="left:14px;top:282px;width:446px;height:246px" role="img" aria-label="Pencil-sketched character holding an application form, a bank statement page, an ID and proof of payment addressed to accounts@qelvo.net"></div>
  <p class="copy" style="left:22px;top:534px;width:444px">-complete application form, page of bank statement, copy of I.D., proof of payment and send to accounts@qelvo.net<br>-Once received, details are loaded onto system and your 4 digit pin is sent to registered cell phone number and email address (Please ensure qelvo! has your correct banking details to enable you to utilise the Utility Wallet.</p>

  <div class="step-no" style="left:502px;top:190px">2</div>
  <div class="step-title" style="left:574px;top:189px;width:346px"><span class="small">How to</span> <span class="big">Top up</span></div>
  <div class="device-label" style="left:486px;top:288px">Phone</div>
  <div class="device phone-frame">DIAL:<br>*120*55501#<br>ENTER 4<br>DIGIT PIN:<br>****<br>SELECT OPTION<br><span style="font-size:11px">1: ENTER AMOUNT</span></div>
  <div class="device-label" style="left:828px;top:276px">Internet</div>
  <div class="device monitor-frame">visit<br><span style="font-size:13px">www.farvolt.net</span><br>click on qelvo<br>login<br>enter pin &amp; cellphone no.<br>purchase</div>
  <p class="copy" style="left:490px;top:580px;width:430px">EFt/ Cash deposit: make payment into qelvo! account specified on application form, use complex name and unit as reference, send proof of payment to accounts@qelvo.net- this method takes 2 days to reflect. R8 transaction fee applies to all top-up purchases made.</p>

  <div class="step-no" style="left:24px;top:698px">3</div>
  <div class="step-title works" style="left:100px;top:694px;width:354px">How does it work?</div>
  <div class="art" style="left:0;top:786px;width:468px;height:218px" role="img" aria-label="Sketch of your unit with a smart meter that communicates to a central server which stores data for a year"></div>
  <p class="copy" style="left:6px;top:1010px;width:462px">-consumers obtains and manages info (balances, statements, consumption reports, usage targets) from servervia internet dashboard.<br>-meter communicates to consumer when credits are low and it is time to top-up.</p>
  <p class="copy center" style="left:6px;top:1078px;width:462px">No disconnections after hours, weekends or public holidays.<br>(Please top up on the next working day to prevent disconnection.)</p>

  <div class="step-no" style="left:502px;top:698px">4</div>
  <div class="step-title off" style="left:574px;top:694px;width:346px">Why is my electricity off?</div>
  <div class="art" style="left:610px;top:792px;width:220px;height:226px" role="img" aria-label="Puzzled pencil-sketched character pointing at a dead light bulb"></div>
  <div class="checklist">
    <h3>PLEASE CHECK THE FOLLOWING</h3>
    <div class="check"><svg width="22" height="20" viewBox="0 0 22 20"><rect x="1" y="4" width="15" height="15" fill="none" stroke="var(--lime)" stroke-width="2"/><path d="M4 11l5 5L21 1" fill="none" stroke="var(--lime)" stroke-width="3"/></svg><span>that the earth leakage and other switches in your DB is on.</span></div>
    <div class="check"><svg width="22" height="20" viewBox="0 0 22 20"><rect x="1" y="4" width="15" height="15" fill="none" stroke="var(--lime)" stroke-width="2"/><path d="M4 11l5 5L21 1" fill="none" stroke="var(--lime)" stroke-width="3"/></svg><span>that your neighbours have electricity.</span></div>
    <div class="check"><svg width="22" height="20" viewBox="0 0 22 20"><rect x="1" y="4" width="15" height="15" fill="none" stroke="var(--lime)" stroke-width="2"/><path d="M4 11l5 5L21 1" fill="none" stroke="var(--lime)" stroke-width="3"/></svg><span>that your account is in a positive balance</span></div>
    <p class="call">After the above points have been confirmed, please phone 071 555 0142<br>for technical assistance</p>
  </div>
</body>
</html>
```